Business Card for Brevel Coatings

We need a simple, yet out standing business card for our painting company.

Target Market(s)

wealthy; high-end neighborhoods, and businesses

Industry/Entity Type

Painting

Contact Information for Business Card

Name:
Doran Vask

Email:
d.vask@brevel-coatings.com

Website:
Brevel-coatings.com

Phone Number:
(555) 416-9073

Font styles to use
Serif
Sans Serif

Requirements
Must have
• slogan "making change simple"
Should not have
• A title attached to the name on the card

```html
<!DOCTYPE html>
<html lang="en">
<head>
<meta charset="utf-8">
<title>Brevel Coatings – Business Card</title>
<link rel="stylesheet" href="https://fonts.googleapis.com/css2?family=Open+Sans:wght@400;600;700&display=swap">
<style>
  :root {
    --backdrop: #8c8c8c;
    --card: #f4f4f4;
    --green-dark: #2f4a12;
    --green-lime: #9ab53a;
    --text: #3e3e3e;
    --white: #ffffff;
  }
  * { margin: 0; padding: 0; box-sizing: border-box; }
  html, body {
    width: 1105px;
    height: 1200px;
    overflow: hidden;
    background: var(--backdrop);
    font-family: "Open Sans", Arial, sans-serif;
  }
  .canvas { position: relative; width: 1105px; height: 1200px; }
  .card {
    position: absolute;
    left: 182px;
    width: 747px;
    height: 427px;
    background: var(--card);
    overflow: hidden;
  }
  .card--front { top: 119px; }
  .card--back { top: 635px; }

  /* front */
  .brand-block {
    position: absolute;
    right: 50px;
    top: 56px;
    text-align: right;
  }
  .brand {
    display: flex;
    align-items: center;
    justify-content: flex-end;
    gap: 14px;
  }
  .brand__mark { width: 30px; height: 30px; background: var(--green-lime); }
  .brand__name {
    font-size: 38px;
    font-weight: 600;
    color: var(--green-dark);
    letter-spacing: 1px;
    line-height: 1;
  }
  .slogan {
    margin-top: 8px;
    font-size: 17px;
    letter-spacing: 3px;
    color: var(--green-lime);
    line-height: 1.2;
  }

  .person { position: absolute; left: 46px; top: 174px; right: 50px; }
  .person__name { font-size: 25px; font-weight: 600; color: var(--green-dark); line-height: 1.2; }
  .person__rule { height: 2px; background: var(--green-dark); margin-top: 12px; }

  .contacts { position: absolute; left: 50px; top: 249px; list-style: none; }
  .contacts li {
    display: flex;
    align-items: center;
    height: 29px;
    font-size: 19px;
    color: var(--text);
  }
  .contacts svg { width: 18px; height: 18px; margin-right: 10px; fill: var(--green-dark); }

  .address {
    position: absolute;
    right: 50px;
    top: 302px;
    text-align: right;
    font-size: 19px;
    font-style: normal;
    line-height: 29px;
    color: var(--text);
  }
  .band { position: absolute; left: 0; bottom: 0; width: 747px; height: 26px; }
  .band__url {
    position: absolute;
    right: 44px;
    bottom: 0;
    height: 26px;
    line-height: 26px;
    font-size: 18px;
    letter-spacing: 3px;
    color: var(--white);
  }

  /* back */
  .back-brand {
    position: absolute;
    left: 0; right: 0;
    top: 180px;
    display: flex;
    justify-content: center;
    align-items: center;
    gap: 16px;
  }
  .back-brand .brand__mark { width: 40px; height: 40px; }
  .back-brand .brand__name { font-size: 50px; }
  .back-url {
    position: absolute;
    left: 0; right: 0;
    top: 359px;
    text-align: center;
    font-size: 19px;
    letter-spacing: 3px;
    color: var(--text);
  }
</style>
</head>
<body>
<main class="canvas">
  <section class="card card--front">
    <div class="brand-block">
      <div class="brand">
        <span class="brand__mark"></span>
        <span class="brand__name">Brevel Coatings</span>
      </div>
      <p class="slogan">making change simple</p>
    </div>

    <div class="person">
      <p class="person__name">Doran Vask</p>
      <div class="person__rule"></div>
    </div>

    <ul class="contacts">
      <li>
        <svg viewBox="0 0 24 24"><path d="M6.6 10.8a15.1 15.1 0 0 0 6.6 6.6l2.2-2.2a1 1 0 0 1 1-.25 11.4 11.4 0 0 0 3.6.57 1 1 0 0 1 1 1V20a1 1 0 0 1-1 1A17 17 0 0 1 3 4a1 1 0 0 1 1-1h3.5a1 1 0 0 1 1 1c0 1.25.2 2.45.57 3.57a1 1 0 0 1-.25 1z"/></svg>
        555 416 9073
      </li>
      <li>
        <svg viewBox="0 0 24 24"><path d="M7 1h10a2 2 0 0 1 2 2v18a2 2 0 0 1-2 2H7a2 2 0 0 1-2-2V3a2 2 0 0 1 2-2zm0 3v14h10V4zm5 15.5a1.2 1.2 0 1 0 0 2.4 1.2 1.2 0 0 0 0-2.4z"/></svg>
        555 208 3417
      </li>
      <li>
        <svg viewBox="0 0 24 24"><path d="M6 2h12v5H6zM3 8h18a2 2 0 0 1 2 2v7h-4v5H5v-5H1v-7a2 2 0 0 1 2-2zm4 8v4h10v-4z"/></svg>
        555 730 6182
      </li>
      <li>
        <svg viewBox="0 0 24 24"><path d="M2 5h20v14H2zm2 2v.5l8 5 8-5V7zm0 2.8V17h16V9.8l-8 5z"/></svg>
        d.vask@brevel-coatings.com
      </li>
    </ul>

    <address class="address">
      4120 Larkspur Court<br>
      Fairhaven, Alaska 34811
    </address>

    <svg class="band" viewBox="0 0 747 26" preserveAspectRatio="none">
      <polygon points="0,0 408,0 384,26 0,26" fill="var(--green-dark)"/>
      <polygon points="422,0 747,0 747,26 396,26" fill="var(--green-lime)"/>
    </svg>
    <span class="band__url">www.brevel-coatings.com</span>
  </section>

  <section class="card card--back">
    <div class="back-brand">
      <span class="brand__mark"></span>
      <span class="brand__name">Brevel Coatings</span>
    </div>
    <p class="back-url">www.brevel-coatings.com</p>
  </section>
</main>
</body>
</html>
```